Brightway Freight Biz Card and Stationary
Brightway Freight
Brightway Freight Biz Card and Stationary -
Creative Brief
Modern
Daniel Prescott
President & CEO
P.O. Box 7382 Harlan Bluff, ND 58217
d.prescott@tarvo.com
keep it simple

```html
<!DOCTYPE html>
<html lang="en">
<head>
<meta charset="utf-8">
<title>Brightway Freight – Business Cards</title>
<link rel="stylesheet" href="https://fonts.googleapis.com/css2?family=Arimo:wght@400;700&display=swap">
<style>
  :root {
    --stage: #1c1c1c;
    --card-white: #ffffff;
    --blue-deep: #0b33c4;
    --blue-mid: #1a73e0;
    --blue-light: #3cb8f2;
    --navy: #1a2f8a;
    --ink: #2a2a2a;
    --muted: #555a66;
  }
  * { margin: 0; padding: 0; box-sizing: border-box; }
  html, body { width: 1200px; height: 854px; overflow: hidden; }
  body {
    position: relative;
    background: var(--stage);
    font-family: "Arimo", Arial, sans-serif;
  }
  .card {
    position: absolute;
    width: 446px;
    height: 258px;
    border-radius: 22px;
    overflow: hidden;
  }
  .card--white { background: var(--card-white); }
  .card--blue {
    background: linear-gradient(120deg, var(--blue-deep) 0%, var(--blue-mid) 45%, var(--blue-light) 100%);
  }
  .card--front-top { left: 120px; top: 108px; }
  .card--back-top { left: 619px; top: 108px; }
  .card--front-bottom { left: 125px; top: 571px; }
  .card--back-bottom { left: 607px; top: 571px; }

  /* front: brand mark */
  .brand-front {
    position: absolute; inset: 0;
    display: flex; flex-direction: column; align-items: center; justify-content: center; gap: 16px;
  }
  .brand-front .brand-dot { width: 96px; height: 96px; border-radius: 50%; }
  .brand-front .brand-name {
    font-weight: 700; font-size: 26px; letter-spacing: 1px; text-transform: uppercase;
  }
  .card--white .brand-dot { background: var(--blue-mid); }
  .card--white .brand-name { color: var(--blue-mid); }
  .card--blue .brand-dot { background: #ffffff; }
  .card--blue .brand-name { color: #ffffff; }

  /* back */
  .brand-back {
    position: absolute; left: 22px; top: 24px;
    display: flex; flex-direction: column; align-items: flex-start; gap: 14px;
  }
  .brand-back .brand-name {
    font-weight: 700; font-size: 17px; letter-spacing: 1px; text-transform: uppercase; width: 150px; line-height: 1.2;
  }
  .brand-back .brand-dot { width: 54px; height: 54px; border-radius: 50%; margin-left: 40px; }
  .card--blue .brand-back .brand-name { color: #fff; }
  .card--blue .brand-back .brand-dot { background: #fff; }
  .card--white .brand-back .brand-name { color: var(--ink); }
  .card--white .brand-back .brand-dot { background: var(--blue-mid); }

  .person { position: absolute; left: 218px; top: 56px; }
  .person-name { font-weight: 700; font-size: 17px; letter-spacing: 0.5px; text-transform: uppercase; }
  .person-title { font-size: 9px; font-weight: 700; text-transform: uppercase; margin-top: 3px; letter-spacing: 0.3px; }
  .card--blue .person-name, .card--blue .person-title { color: #fff; }
  .card--white .person-name, .card--white .person-title { color: var(--navy); }

  .contacts { position: absolute; left: 208px; top: 100px; list-style: none; }
  .contacts li { display: flex; align-items: center; gap: 10px; height: 27px; font-size: 11px; }
  .contacts svg { width: 18px; height: 18px; flex: none; fill: none; stroke-width: 1.6; stroke-linecap: round; stroke-linejoin: round; }
  .contacts .contact-address { height: 34px; }
  .card--blue .contacts li { color: #fff; }
  .card--blue .contacts svg { stroke: #fff; }
  .card--white .contacts li { color: var(--muted); }
  .card--white .contacts svg { stroke: var(--muted); }
  .address { line-height: 1.25; }
</style>
</head>
<body>

  <section class="card card--white card--front-top">
    <div class="brand-front"><span class="brand-dot"></span><span class="brand-name">Brightway Freight</span></div>
  </section>

  <section class="card card--blue card--back-top">
    <div class="brand-back"><span class="brand-name">Brightway Freight</span><span class="brand-dot"></span></div>
    <div class="person"><p class="person-name">Daniel Prescott</p><p class="person-title">President &amp; CEO</p></div>
    <ul class="contacts">
      <li class="contact-address"><svg viewBox="0 0 20 20"><circle cx="10" cy="10" r="8"/><path d="M2 10h16M10 2c3 3 3 13 0 16M10 2c-3 3-3 13 0 16"/></svg><span class="address">P.O. Box 7382<br>Harlan Bluff, ND 58217</span></li>
      <li><svg viewBox="0 0 20 20"><rect x="6" y="2" width="8" height="16" rx="1.5"/><path d="M9 15h2"/></svg><span>701 555 0148</span></li>
      <li><svg viewBox="0 0 20 20"><path d="M5 3l3 0 1 4-2 1.5c1 2 2.5 3.5 4.5 4.5L13 11l4 1v3c0 1-1 2-2 2C9 17 3 11 3 5c0-1 1-2 2-2z"/></svg><span>701 555 0162</span></li>
      <li><svg viewBox="0 0 20 20"><rect x="3" y="7" width="14" height="9" rx="1"/><path d="M6 7V3h8v4M6 12h8"/></svg><span>888 555 0193</span></li>
      <li><svg viewBox="0 0 20 20"><rect x="2" y="4" width="16" height="12" rx="1"/><path d="M2 5l8 6 8-6"/></svg><span>d.prescott@tarvo.com</span></li>
    </ul>
  </section>

  <section class="card card--blue card--front-bottom">
    <div class="brand-front"><span class="brand-dot"></span><span class="brand-name">Brightway Freight</span></div>
  </section>

  <section class="card card--white card--back-bottom">
    <div class="brand-back"><span class="brand-name">Brightway Freight</span><span class="brand-dot"></span></div>
    <div class="person"><p class="person-name">Daniel Prescott</p><p class="person-title">President &amp; CEO</p></div>
    <ul class="contacts">
      <li class="contact-address"><svg viewBox="0 0 20 20"><circle cx="10" cy="10" r="8"/><path d="M2 10h16M10 2c3 3 3 13 0 16M10 2c-3 3-3 13 0 16"/></svg><span class="address">P.O. Box 7382<br>Harlan Bluff, ND 58217</span></li>
      <li><svg viewBox="0 0 20 20"><rect x="6" y="2" width="8" height="16" rx="1.5"/><path d="M9 15h2"/></svg><span>701 555 0148</span></li>
      <li><svg viewBox="0 0 20 20"><path d="M5 3l3 0 1 4-2 1.5c1 2 2.5 3.5 4.5 4.5L13 11l4 1v3c0 1-1 2-2 2C9 17 3 11 3 5c0-1 1-2 2-2z"/></svg><span>701 555 0162</span></li>
      <li><svg viewBox="0 0 20 20"><rect x="3" y="7" width="14" height="9" rx="1"/><path d="M6 7V3h8v4M6 12h8"/></svg><span>888 555 0193</span></li>
      <li><svg viewBox="0 0 20 20"><rect x="2" y="4" width="16" height="12" rx="1"/><path d="M2 5l8 6 8-6"/></svg><span>d.prescott@tarvo.com</span></li>
    </ul>
  </section>

</body>
</html>
```